New Label Design Project

DetailHi, we are a small Farm growing and selling fresh and dehydrated exotic vegetables to exotic market and ethnic restaurants. We plan to make changes our packaging by using clamshell instead of bags. This is why we send you this project. Our main Target Market are Jamaican, Haitian, Egyptian and Turkish restaurant. Small supermarket Markets like Zelto, Marcovina, Lunbrook Food Market, Quill food Market.... I sale to reseller in some farmers Market in Florida and Massachusetts. Then we have some direct customers they pick it at the farm stand. We don't have any online presence, my apologies... We are still working on that... We send you different logo. We are still working on the sizes of the clamshell. s for my new Label Design Project will be added soon.

```html
<!DOCTYPE html>
<html lang="en">
<head>
<meta charset="utf-8">
<title>Fenwick Farm – Exotic Dried Mixed Vegetables Label</title>
<link rel="stylesheet" href="https://fonts.googleapis.com/css2?family=League+Spartan:wght@700;800&family=Jost:wght@400;500&display=swap">
<style>
  :root {
    --forest: #41552f;
    --leaf: #84a862;
    --leaf-soft: #93b573;
    --paper: #ffffff;
  }
  * { margin: 0; padding: 0; box-sizing: border-box; }
  html, body { width: 1200px; height: 600px; overflow: hidden; }
  body {
    background: var(--forest);
    position: relative;
    font-family: "Jost", "Helvetica Neue", Arial, sans-serif;
  }

  /* Lid label */
  .lid-label {
    position: absolute;
    left: 70px; top: 116px;
    width: 660px; height: 368px;
    background: var(--paper);
    border-radius: 46px;
    overflow: hidden;
  }
  .claims-panel {
    position: absolute;
    left: 0; top: 0;
    width: 272px; height: 100%;
    background: var(--leaf);
  }
  .vegetable-artwork {
    position: absolute;
    left: 14px; top: 12px;
    width: 244px; height: 244px;
    border-radius: 28px 6px 6px 6px;
    background: linear-gradient(150deg, var(--leaf-soft), var(--leaf));
  }
  .claims-list {
    position: absolute;
    left: 0; top: 272px;
    width: 100%;
    color: var(--paper);
    font-size: 15px;
    line-height: 19px;
    text-align: center;
    letter-spacing: 0.2px;
  }
  .net-weight {
    position: absolute;
    left: 0; top: 322px;
    width: 100%;
    text-align: center;
    color: var(--paper);
    font-size: 17px;
    font-weight: 500;
  }

  .product-title {
    position: absolute;
    left: 296px; top: 46px;
    color: var(--leaf);
    font-family: "League Spartan", "Arial Black", sans-serif;
    font-weight: 800;
    line-height: 1;
  }
  .title-rule {
    width: 222px; height: 9px;
    background: var(--leaf);
    margin-bottom: 12px;
  }
  .title-exotic { font-size: 52px; letter-spacing: -0.5px; height: 50px; }
  .title-dried, .title-mixed { font-size: 82px; letter-spacing: -1px; height: 76px; }
  .title-dried { margin-top: 6px; }
  .title-veg { font-size: 42px; letter-spacing: -0.3px; height: 40px; margin-top: 6px; }

  .organic-claim {
    position: absolute;
    left: 298px; top: 324px;
    color: var(--leaf);
    font-size: 20px;
    letter-spacing: 0.4px;
  }

  .brand-lockup {
    position: absolute;
    right: 24px; top: 42px;
    width: 100px;
    text-align: center;
    color: var(--leaf);
  }
  .brand-dot {
    width: 30px; height: 30px;
    margin: 0 auto 8px;
    border-radius: 50%;
    background: var(--leaf);
  }
  .brand-name { font-size: 13px; font-weight: 500; letter-spacing: 0.2px; }
  .brand-tagline { font-size: 6px; letter-spacing: 0.2px; }

  /* Round side sticker */
  .side-sticker {
    position: absolute;
    left: 800px; top: 150px;
    width: 300px; height: 300px;
    border-radius: 50%;
    background: var(--leaf);
    color: var(--paper);
    text-align: center;
  }
  .sticker-dot {
    position: absolute;
    left: 110px; top: 52px;
    width: 80px; height: 80px;
    border-radius: 50%;
    background: var(--paper);
  }
  .sticker-name {
    position: absolute;
    left: 0; top: 170px;
    width: 100%;
    font-size: 34px;
    font-weight: 500;
    letter-spacing: 0.3px;
  }
  .sticker-tagline {
    position: absolute;
    left: 0; top: 214px;
    width: 100%;
    font-size: 14px;
    font-weight: 500;
    letter-spacing: 0.3px;
  }
</style>
</head>
<body>

  <section class="lid-label">
    <div class="claims-panel">
      <div class="vegetable-artwork" role="img" aria-label="Line drawings of vegetables: tomato, eggplant, onion, beet, carrot, broccoli, spinach, pepper, radish and bitter gourd"></div>
      <p class="claims-list">• NON GMO &nbsp;• LOW CALORIE<br>• LOW CARB &nbsp;• GLUTEN FREE</p>
      <p class="net-weight">60 g</p>
    </div>

    <h1 class="product-title">
      <div class="title-rule"></div>
      <div class="title-exotic">EXOTIC</div>
      <div class="title-dried">DRIED</div>
      <div class="title-mixed">MIXED</div>
      <div class="title-veg">VEGETABLES</div>
    </h1>
    <p class="organic-claim">100% ORGANIC</p>

    <div class="brand-lockup">
      <div class="brand-dot"></div>
      <p class="brand-name">FENWICK FARM</p>
      <p class="brand-tagline">ROOTED IN GOOD SOIL</p>
    </div>
  </section>

  <section class="side-sticker">
    <div class="sticker-dot"></div>
    <p class="sticker-name">FENWICK FARM</p>
    <p class="sticker-tagline">ROOTED IN GOOD SOIL</p>
  </section>

</body>
</html>
```